Bluewater Motor Finance Home Page

We need a desktop version mock up (we will base our mobile version off of this) of a website homepage for our auto loan business, Bluewater Motor Finance. This does not need to be a functioning site, just a home page mock up. We are based in the metro St. Louis, MO area. We offer "guaranteed" auto loans for all credit types. We specialize in financing for bad/no credit customers. We are able to help rebuild these type of customers' credit, all while putting them in a great late model vehicle they'll love. Our online credit app takes less than 60 seconds, doesn't require a SS# and gives a free credit score if they fill it out within 3 minutes. We are looking for an outside perspective to help us in this design process. We are not completely sure what we want, but we do want it to be professional and secure looking, all while being unique and aesthetically pleasing. We want the customer to be able to put in their zip code to be directed to the right location that can get them pre approved. I attached a wireframe with some stuff we'd like to include, but in no way does it have to be in the same layout or the same ideas. We want everyone to "go crazy" with their creative side on this. Our current site is awful, here is a link to get a better idea: www.bluewatermotorfinance-example.com. Attached is our logo too, base colors off of it. Watch our video that is also attached for a better idea.

Target Market(s)

Residents of the St. Louis Missouri Metro Area that need an auto loan. 24-55 Male and Female - Lots of "urban market" customers.

Industry/Entity Type

Loan

Number of Pages Required

1 page

Colors
9bcb3b

Requirements
Must have
• An area where the customer can enter their zip code - Be creative!
Nice to have
• See wireframe attachment for ideas - Be creative!

```html
<!DOCTYPE html>
<html lang="en">
<head>
<meta charset="utf-8">
<title>Bluewater Motor Finance – Home</title>
<link href="https://fonts.googleapis.com/css2?family=Open+Sans:wght@400;600;700;800&family=Oswald:wght@400;500&display=swap" rel="stylesheet">
<style>
:root{
  --green:#1fae4b;
  --green-dark:#168a3a;
  --yellow:#f3ea1c;
  --beige:#efe9da;
  --paper:#eeebe6;
  --orange:#f7931e;
  --teal:#4fd1a5;
  --blue:#1ab2dd;
  --coral:#fb6352;
  --slate:#6a8995;
  --footer:#333333;
  --ink:#333333;
  --muted:#666666;
  --white:#ffffff;
}
*{box-sizing:border-box;margin:0;padding:0}
html,body{width:1200px;height:3093px;overflow:hidden}
body{position:relative;font-family:"Open Sans",Arial,sans-serif;color:var(--ink);background:var(--white)}
.abs{position:absolute}

/* header */
.site-header{position:absolute;left:0;top:0;width:1200px;height:107px;background:var(--white);border-bottom:2px solid #e4e4e4}
.brand{position:absolute;left:74px;top:35px;display:flex;align-items:center;gap:10px;font-weight:800;font-size:18px;color:var(--green);white-space:nowrap}
.brand-square{width:32px;height:32px;background:var(--green)}
.main-nav{position:absolute;left:404px;top:40px;display:flex;gap:22px;font-family:"Oswald",Arial,sans-serif;font-size:17px;color:#444;letter-spacing:.4px;white-space:nowrap}
.phone-pill{position:absolute;left:897px;top:29px;width:231px;height:47px;border-radius:24px;background:var(--green);border:3px solid var(--yellow);display:flex;align-items:center;padding-left:66px;font-family:"Oswald",Arial,sans-serif;font-size:23px;color:var(--white)}
.phone-pill .phone-badge{position:absolute;left:-3px;top:-3px;width:66px;height:47px;border-radius:24px;background:var(--yellow);display:flex;align-items:center;justify-content:center}

/* hero */
.hero{position:absolute;left:0;top:107px;width:1200px;height:441px;background:linear-gradient(100deg,#1d1a16 0%,#3a3026 30%,#5a4a36 45%,#2a2824 65%,#4a4a46 85%,#1a1a1a 100%)}
.hero-title{position:absolute;left:0;top:58px;width:1200px;text-align:center;color:var(--white);font-weight:700;font-size:39px}
.hero-title em{font-style:normal;color:var(--yellow)}
.hero-sub{position:absolute;left:0;top:108px;width:1200px;text-align:center;color:var(--white);font-weight:600;font-size:23px}
.zip-form{position:absolute;left:289px;top:202px;width:635px;height:77px;border-radius:39px;background:var(--green);padding:9px}
.zip-field{width:100%;height:100%;border-radius:30px;background:var(--white);display:flex;align-items:center;padding-left:30px;font-size:22px;color:#777;position:relative}
.zip-btn{position:absolute;right:6px;top:6px;width:216px;height:47px;border-radius:24px;background:var(--yellow);border:2px solid #222;display:flex;align-items:center;justify-content:center;font-weight:800;font-size:19px;color:#222}
.features{position:absolute;left:0;top:493px;width:1200px;height:90px;z-index:2}
.feature{position:absolute;top:16px;width:244px;height:68px;background:var(--white);border-radius:34px;display:flex;align-items:center;justify-content:center;text-align:center;font-size:13px;line-height:1.3;color:#333;padding-top:4px}
.feature-icon{position:absolute;top:-24px;left:2px;width:54px;height:54px;border-radius:50%;background:var(--green);border:3px solid var(--white);display:flex;align-items:center;justify-content:center}

/* apply band */
.apply-band{position:absolute;left:0;top:548px;width:1200px;height:116px;background:var(--yellow)}
.apply-line{position:absolute;left:0;top:40px;width:1200px;display:flex;justify-content:center;align-items:center;gap:12px;font-size:22px;color:#333}
.timer{width:72px;height:56px;border-radius:28px;background:var(--green);color:var(--white);font-weight:700;display:flex;align-items:center;justify-content:center}

/* testimonial */
.testimonial{position:absolute;left:0;top:664px;width:1200px;height:357px;background:var(--beige)}
.testimonial .eyebrow{position:absolute;top:60px;width:1200px;text-align:center;font-size:15px;letter-spacing:4px;color:#444}
.testimonial h2{position:absolute;top:80px;width:1200px;text-align:center;font-weight:400;font-size:31px;letter-spacing:1px;color:#222}
.testimonial .rule{position:absolute;left:586px;top:126px;width:28px;height:3px;background:var(--green)}
.quote-mark{position:absolute;top:158px;font-size:60px;font-weight:800;color:var(--green);line-height:1}
.quote-text{position:absolute;left:250px;top:158px;width:700px;text-align:center;font-size:16px;line-height:1.55;color:#555}
.quote-name{position:absolute;top:240px;width:1200px;text-align:center;font-weight:700;font-size:17px;color:var(--green)}
.quote-date{position:absolute;top:264px;width:1200px;text-align:center;font-size:13px;color:#777}

/* calculator */
.calc{position:absolute;left:0;top:1021px;width:1200px;height:268px;background:var(--paper)}
.calc-art{position:absolute;left:120px;top:41px;width:169px;height:169px;border-radius:8px;background:linear-gradient(135deg,#9aa1a6,#d7dadd 50%,#3b6fb0)}
.calc-copy{position:absolute;left:340px;top:88px;width:510px;text-align:center;font-weight:600;font-size:18px;line-height:1.45;color:#333}
.calc-btn{position:absolute;left:876px;top:82px;width:250px;height:52px;background:var(--orange);border-radius:3px;display:flex;align-items:center;justify-content:center;color:var(--white);font-weight:700;font-size:18px;box-shadow:0 3px 0 #d97b0f}

/* steps */
.steps{position:absolute;left:0;top:1289px;width:1200px;height:1072px}
.step-circle{position:absolute;width:296px;height:296px;border-radius:50%;background:var(--white);border:8px solid #e2e2e2;display:flex;align-items:center;justify-content:center}
.step-copy{position:absolute;width:510px;color:var(--white);font-size:13.5px;line-height:24px}
.step-copy h3{font-size:21px;font-weight:700;margin-bottom:6px}
.step-copy.right{text-align:right}

/* about */
.about{position:absolute;left:0;top:2361px;width:1200px;height:423px;background:var(--slate)}
.about h2{position:absolute;left:74px;top:66px;font-size:22px;font-weight:700;color:var(--white)}
.about p{position:absolute;left:74px;top:108px;width:420px;font-size:13.5px;line-height:24px;color:var(--white)}
.video{position:absolute;left:551px;top:58px;width:548px;height:309px;background:linear-gradient(120deg,#d9d2c6,#bfb3a3 40%,#8a7c8a 70%,#e6e1d8)}
.play{position:absolute;left:233px;top:113px;width:82px;height:82px;border-radius:50%;border:5px solid var(--white);display:flex;align-items:center;justify-content:center}

/* footer */
.site-footer{position:absolute;left:0;top:2784px;width:1200px;height:247px;background:var(--footer);color:#ddd}
.contact{position:absolute;top:40px;display:flex;gap:14px}
.contact-text{border-left:2px solid var(--yellow);padding-left:14px;font-size:14px;line-height:25px}
.contact-text small{display:block;font-size:11px;letter-spacing:1px;color:#bbb}
.msg-btn{display:inline-block;margin-top:10px;padding:4px 14px;border-radius:14px;background:var(--yellow);color:#222;font-weight:700;font-size:13px}
.social{display:inline-block;width:28px;height:28px;border-radius:50%;border:2px solid #ddd;vertical-align:middle;margin-left:6px}
.footer-nav{position:absolute;top:192px;width:1200px;display:flex;justify-content:center;gap:38px;font-weight:700;font-size:13px;color:var(--white)}
.legal{position:absolute;left:0;top:3031px;width:1200px;height:62px;background:var(--green);color:var(--white);text-align:center;font-size:12.5px;line-height:19px;padding-top:12px}
</style>
</head>
<body>

<header class="site-header">
  <div class="brand"><span class="brand-square"></span>Bluewater Motor Finance</div>
  <nav class="main-nav"><span>LOCATIONS</span><span>FINANCE CENTER</span><span>ABOUT</span><span>FAQ</span><span>CONTACT</span></nav>
  <div class="phone-pill">
    <span class="phone-badge"><svg width="26" height="26" viewBox="0 0 24 24"><path d="M6.6 10.8a15 15 0 0 0 6.6 6.6l2.2-2.2c.3-.3.7-.4 1-.2 1.1.4 2.3.6 3.6.6.6 0 1 .4 1 1V20c0 .6-.4 1-1 1A17 17 0 0 1 3 4c0-.6.4-1 1-1h3.5c.6 0 1 .4 1 1 0 1.3.2 2.5.6 3.6.1.3 0 .7-.2 1z" fill="#168a3a"/></svg></span>
    (800) 555-0142
  </div>
</header>

<section class="hero" role="img" aria-label="Night-time view from the driver's seat of a car on a blurred city road">
  <h1 class="hero-title">Over <em>30,000</em> Auto Loans Since 2000</h1>
  <p class="hero-sub">Pre-Approval in Under 60 Seconds!</p>
  <div class="zip-form">
    <div class="zip-field">Enter zip code<span class="zip-btn">GET APPROVED</span></div>
  </div>
</section>

<section class="apply-band">
  <p class="apply-line">Apply within <span class="timer">3:00</span> and see your credit score for free!</p>
</section>

<div class="features">
  <div class="feature" style="left:87px"><span class="feature-icon"><svg width="28" height="28" viewBox="0 0 24 24"><path d="M12 2l8 3v6c0 5-3.5 9-8 11-4.5-2-8-6-8-11V5z" fill="none" stroke="#fff" stroke-width="2"/><path d="M8 8l8 8M16 8l-8 8" stroke="#fff" stroke-width="2"/></svg></span>No Social Security<br>Number Required</div>
  <div class="feature" style="left:348px"><span class="feature-icon"><svg width="28" height="28" viewBox="0 0 24 24"><circle cx="12" cy="12" r="10" fill="#fff"/><path d="M7 12l3.5 3.5L17 9" fill="none" stroke="#1fae4b" stroke-width="2.6"/></svg></span>Instant Approval</div>
  <div class="feature" style="left:608px"><span class="feature-icon"><svg width="28" height="28" viewBox="0 0 24 24"><circle cx="11" cy="11" r="8" fill="none" stroke="#fff" stroke-width="2"/><text x="11" y="15" font-size="10" font-weight="700" fill="#fff" text-anchor="middle" font-family="Open Sans, sans-serif">$</text><path d="M16 16l6 6M22 16l-6 6" stroke="#fff" stroke-width="2"/></svg></span>No Application Fees</div>
  <div class="feature" style="left:868px"><span class="feature-icon"><svg width="28" height="28" viewBox="0 0 24 24"><rect x="3" y="5" width="18" height="13" rx="2" fill="none" stroke="#fff" stroke-width="2"/><rect x="3" y="8" width="18" height="3" fill="#fff"/><path d="M14 15h5" stroke="#fff" stroke-width="2"/></svg></span>All Credit Accepted</div>
</div>

<section class="testimonial">
  <p class="eyebrow">OUR</p>
  <h2>TESTIMONIAL</h2>
  <span class="rule"></span>
  <span class="quote-mark" style="left:184px">&ldquo;</span>
  <p class="quote-text">Overall very pleasant. I was given option that would work for me, which I appreciated.<br>Very happy with the outcome!.</p>
  <span class="quote-mark" style="left:972px">&rdquo;</span>
  <p class="quote-name">Marcus T.</p>
  <p class="quote-date">10/17/15</p>
</section>

<section class="calc">
  <div class="calc-art" role="img" aria-label="Calculator resting on bank cards"></div>
  <p class="calc-copy">Lorem ipsum dolor sit amet, consectetur adipiscing elit.<br>Proin a elit vitae erat accumsan.</p>
  <span class="calc-btn">CALCULATE PAYMENT</span>
</section>

<section class="steps">
  <svg class="abs" style="left:0;top:0" width="1200" height="1072" viewBox="0 1289 1200 1072">
    <polygon points="0,1423 1200,1295 1200,1612 0,1592" fill="#4fd1a5"/>
    <polygon points="0,1578 1200,1598 1200,1612 0,1592" fill="#3fbf93"/>
    <polygon points="0,1623 1200,1722 1200,1907 0,1938" fill="#1ab2dd"/>
    <polygon points="0,2062 1200,1955 1200,2268 0,2268" fill="#fb6352"/>
  </svg>

  <div class="step-circle" style="left:91px;top:39px">
    <svg width="170" height="170" viewBox="0 0 100 100"><polygon points="50,4 61,14 76,12 80,27 94,34 88,48 94,62 80,69 76,84 61,82 50,94 39,82 24,84 20,69 6,62 12,48 6,34 20,27 24,12 39,14" fill="#666"/><path d="M31 50l13 13 25-26" fill="none" stroke="#fff" stroke-width="9"/></svg>
  </div>
  <div class="step-copy" style="left:433px;top:106px">
    <h3>STEP 1</h3>
    <p>Lorem ipsum dolor sit amet, consectetur adipiscing elit, sed do eiusmod tempor incididunt ut labore et dolore magna aliqua. Ut enim ad minim veniam, quis nostrud exercitation ullamco laboris nisi ut aliquip ex ea commodo consequat. Duis aute irure dolor in reprehenderit in voluptate velit esse cillum dolore eu fugiat nulla pariatur. Excepteur sint occaecat cupidatat non proident, sunt in culpa qui officia deserunt mollit anim id est laborum.</p>
  </div>

  <div class="step-circle" style="left:811px;top:361px">
    <svg width="170" height="170" viewBox="0 0 100 100"><path d="M84 42A35 35 0 1 1 62 17" fill="none" stroke="#666" stroke-width="8"/><polygon points="56,4 78,18 56,30" fill="#666"/><circle cx="50" cy="42" r="12" fill="#666"/><path d="M26 78c2-14 12-20 24-20s22 6 24 20z" fill="#666"/></svg>
  </div>
  <div class="step-copy right" style="left:257px;top:429px">
    <h3>STEP 2</h3>
    <p>Lorem ipsum dolor sit amet, consectetur adipiscing elit, sed do eiusmod tempor incididunt ut labore et dolore magna aliqua. Ut enim ad minim veniam, quis nostrud exercitation ullamco laboris nisi ut aliquip ex ea commodo consequat. Duis aute irure dolor in reprehenderit in voluptate velit esse cillum dolore eu fugiat nulla pariatur. Excepteur sint occaecat cupidatat non proident, sunt in culpa qui officia deserunt mollit anim id est laborum.</p>
  </div>

  <div class="step-circle" style="left:91px;top:695px">
    <svg width="170" height="170" viewBox="0 0 100 100"><g transform="rotate(45 50 50)"><path d="M50 6c12 12 14 30 10 52H40c-4-22-2-40 10-52z" fill="#666"/><path d="M40 44l-12 16v10l12-8zM60 44l12 16v10l-12-8z" fill="#666"/><circle cx="50" cy="32" r="6" fill="#fff"/><path d="M44 64h4v16h-4zM52 64h4v22h-4z" fill="#666"/></g></svg>
  </div>
  <div class="step-copy" style="left:433px;top:762px">
    <h3>STEP 3</h3>
    <p>Lorem ipsum dolor sit amet, consectetur adipiscing elit, sed do eiusmod tempor incididunt ut labore et dolore magna aliqua. Ut enim ad minim veniam, quis nostrud exercitation ullamco laboris nisi ut aliquip ex ea commodo consequat. Duis aute irure dolor in reprehenderit in voluptate velit esse cillum dolore eu fugiat nulla pariatur. Excepteur sint occaecat cupidatat non proident, sunt in culpa qui officia deserunt mollit anim id est laborum.</p>
  </div>
</section>

<section class="about">
  <h2>BLUEWATER MOTOR FINANCE</h2>
  <p>Lorem ipsum dolor sit amet, consectetur adipiscing elit, sed do eiusmod tempor incididunt ut labore et dolore magna aliqua. Ut enim ad minim veniam, quis nostrud exercitation ullamco laboris nisi ut aliquip ex ea commodo consequat. Duis aute irure dolor in reprehenderit in voluptate velit esse cillum dolore eu fugiat nulla pariatur. Excepteur sint occaecat cupidatat non proident, sunt in culpa qui officia deserunt mollit anim id est laborum.</p>
  <div class="video" role="img" aria-label="Video still of a couple reviewing their finances at home">
    <span class="play"><svg width="34" height="34" viewBox="0 0 24 24"><polygon points="7,4 20,12 7,20" fill="#fff"/></svg></span>
  </div>
</section>

<footer class="site-footer">
  <div class="contact" style="left:224px">
    <svg width="26" height="34" viewBox="0 0 24 32"><path d="M12 2a9 9 0 0 0-9 9c0 7 9 19 9 19s9-12 9-19a9 9 0 0 0-9-9z" fill="none" stroke="#f3ea1c" stroke-width="2.4"/><circle cx="12" cy="11" r="3.5" fill="none" stroke="#f3ea1c" stroke-width="2.4"/></svg>
    <div class="contact-text"><small>VISIT</small>Your Company LTD.<br>Street Name, 000000<br>City Name</div>
  </div>
  <div class="contact" style="left:484px">
    <svg width="30" height="30" viewBox="0 0 24 24"><path d="M6.6 10.8a15 15 0 0 0 6.6 6.6l2.2-2.2c.3-.3.7-.4 1-.2 1.1.4 2.3.6 3.6.6.6 0 1 .4 1 1V20c0 .6-.4 1-1 1A17 17 0 0 1 3 4c0-.6.4-1 1-1h3.5c.6 0 1 .4 1 1 0 1.3.2 2.5.6 3.6.1.3 0 .7-.2 1z" fill="none" stroke="#f3ea1c" stroke-width="1.8"/></svg>
    <div class="contact-text"><small>CALL</small>(800) 555-0142</div>
  </div>
  <div class="contact" style="left:718px">
    <svg width="30" height="30" viewBox="0 0 24 24"><path d="M4 20l2-6L17 3l4 4L10 18z" fill="none" stroke="#f3ea1c" stroke-width="1.8"/><path d="M4 20l6-2" stroke="#f3ea1c" stroke-width="1.8"/></svg>
    <div class="contact-text"><small>WRITE</small>info@bluewatermotorfinance-example.com<br><span class="msg-btn">MESSAGE US</span><span class="social"></span><span class="social"></span></div>
  </div>
  <nav class="footer-nav"><span>HOME</span><span>ABOUT</span><span>PRIVACY</span><span>CONTACT</span></nav>
</footer>
<div class="legal">© 2016 Bluewater Motor Finance. All Rights Reserved<br>Created by Northpoint Studio.</div>

</body>
</html>
```